Business Card for an electrical contractor involved in the resource industry
KLM Partners Australia
Business Card for an electrical contractor involved in the resource industry - Construction
Creative Brief
Simple
Derek Fanshaw
Managing Director
Head Office Suite 2716, 58, Moreland St Carrow Flats, NSW 2039
derek@klmpartnersaustralia.com.au
www.klmpartnersaustralia.com.au
Web Address and logo

```html
<!DOCTYPE html>
<html lang="en">
<head>
<meta charset="UTF-8">
<title>Halvorsen Electrical – Business Card</title>
<link rel="stylesheet" href="https://fonts.googleapis.com/css2?family=Roboto:wght@300;400;700&display=swap">
<style>
  :root {
    --backdrop: #d9d7d3;
    --card: #ffffff;
    --red: #c8102e;
    --red-dark: #9e0b22;
    --red-light: #e0303f;
    --ink: #333333;
    --muted: #8a8a8a;
  }
  * { margin: 0; padding: 0; box-sizing: border-box; }
  html, body {
    width: 1200px; height: 940px; overflow: hidden;
    background: var(--backdrop);
    font-family: "Roboto", Arial, sans-serif;
  }
  .card {
    position: absolute; left: 370px; top: 70px;
    width: 460px; height: 800px;
    background: var(--card);
    border-radius: 34px;
    box-shadow: 0 10px 30px rgba(0,0,0,0.18);
    overflow: hidden;
  }
  .brand {
    position: absolute; left: 48px; top: 120px;
    display: flex; align-items: center; gap: 14px;
  }
  .brand-mark {
    width: 40px; height: 40px; background: var(--red); flex: none;
  }
  .brand-name {
    color: var(--red); font-weight: 400; font-size: 26px; letter-spacing: 0.3px;
    white-space: nowrap;
  }
  .brand-tagline {
    position: absolute; left: 102px; top: 166px;
    font-size: 11px; color: var(--muted); letter-spacing: 0.6px;
  }
  .band-rule {
    position: absolute; left: 0; width: 100%; height: 3px; background: var(--red);
  }
  .band-rule.top { top: 232px; }
  .band-rule.bottom { top: 380px; }
  .band {
    position: absolute; left: 0; top: 244px; width: 100%; height: 126px;
    background: linear-gradient(90deg, var(--red-dark), var(--red-light) 50%, var(--red-dark));
    padding: 30px 48px 0;
    color: #fff;
  }
  .person-name {
    font-size: 32px; font-weight: 300; letter-spacing: 1px; text-transform: uppercase;
    white-space: nowrap;
  }
  .person-title {
    margin-top: 6px; font-size: 20px; font-weight: 400;
  }
  .contacts {
    position: absolute; left: 48px; top: 420px;
    list-style: none; color: var(--ink); font-size: 16px; line-height: 1.6;
    white-space: nowrap;
  }
</style>
</head>
<body>
  <section class="card">
    <div class="brand">
      <span class="brand-mark"></span>
      <span class="brand-name">Halvorsen Electrical</span>
    </div>
    <p class="brand-tagline">Electrical Solutions for Resources</p>

    <div class="band-rule top"></div>
    <div class="band">
      <p class="person-name">Derek Fanshaw</p>
      <p class="person-title">Managing Director</p>
    </div>
    <div class="band-rule bottom"></div>

    <ul class="contacts">
      <li>Suite 2716, 58, Moreland St, Carrow Flats, NSW 2039</li>
      <li>012 555 0147</li>
      <li>derek@halvorsenelectrical.com.au</li>
      <li>www.halvorsenelectrical.com.au</li>
    </ul>
  </section>
</body>
</html>
```